Geschäftspapiere/Rechnungspapier für Mountainbike-Kurse & -events
Hallo,
die Firma kurvenrad organisiert Mountainbike Fahrtechnik Kurse und veranstaltet Bike Events für Firmen.
Das kann ein Bike Betriebsausflug sein oder ein Bikecamp über das Wochenende.
Aufgabenstellung
- das Logo muss drauf auf das Briefpapier
- Meine Kontaktdaten müssen drauf sein
- es muss hübsch ausschauen und Professionell wirken
- Es muss erkennbar sein am Design was ich mache bzw. ersichtlich das es etwas mit Radsport zutun hat
- Firmenname: kurvenrad
- Schwerpunkt: Fahrtechnik Mountainbike / Individuelle Firmen Events / Guiding

```html
<!DOCTYPE html>
<html lang="de">
<head>
<meta charset="utf-8">
<title>kurvenrad – Briefpapier</title>
<link rel="stylesheet" href="https://fonts.googleapis.com/css2?family=Open+Sans:wght@400;600&display=swap">
<style>
  :root {
    --orange: #f29123;
    --grey: #9a9a9a;
    --paper: #ffffff;
    --faint: #f3f3f3;
  }
  html, body {
    margin: 0;
    padding: 0;
    overflow: hidden;
    background: var(--paper);
  }
  .sheet {
    position: relative;
    width: 848px;
    height: 1200px;
    overflow: hidden;
    background: var(--paper);
    font-family: "Open Sans", Arial, sans-serif;
    color: var(--grey);
  }
  .return-line {
    position: absolute;
    left: 81px;
    top: 179px;
    font-size: 8.6px;
    letter-spacing: -0.1px;
    white-space: nowrap;
  }
  .return-line .brand { color: var(--orange); }
  .brand-mark {
    position: absolute;
    left: 624px;
    top: 40px;
    width: 182px;
    height: 182px;
    box-sizing: border-box;
    border: 3.5px solid var(--orange);
    border-radius: 50%;
    display: flex;
    align-items: center;
    justify-content: center;
  }
  .brand-mark .name {
    font-size: 27px;
    font-weight: 600;
    color: var(--orange);
    letter-spacing: 0.3px;
  }
  .tagline {
    position: absolute;
    left: 560px;
    width: 314px;
    top: 234px;
    margin: 0;
    text-align: center;
    color: var(--orange);
    font-size: 17.5px;
    font-weight: 400;
    line-height: 22.5px;
  }
  .contact {
    position: absolute;
    left: 653px;
    top: 319px;
    font-size: 11.4px;
    line-height: 15.7px;
  }
  .contact section { margin-bottom: 6.8px; }
  .contact h2 {
    margin: 0;
    font-size: 11.4px;
    font-weight: 400;
    color: var(--orange);
  }
  .contact h2.company { font-weight: 600; }
  .contact p { margin: 0; }
  .scenery {
    position: absolute;
    left: 72px;
    top: 790px;
    width: 710px;
    height: 373px;
    background: linear-gradient(to bottom, rgba(243,243,243,0) 0%, var(--faint) 35%, var(--faint) 100%);
    border-radius: 50% 50% 0 0 / 40% 40% 0 0;
  }
  .footer-band {
    position: absolute;
    left: 0;
    bottom: 0;
    width: 848px;
    height: 17px;
    background: var(--orange);
  }
</style>
</head>
<body>
<div class="sheet">
  <div class="scenery" role="img" aria-label="Blasse Hintergrundillustration: Berglandschaft mit Tannen, Serpentinenweg und Mountainbike"></div>

  <div class="return-line"><span class="brand">kurvenrad</span> · Musterstraße 25/1 · 12345 Musterstadt</div>

  <div class="brand-mark"><span class="name">kurvenrad</span></div>

  <h1 class="tagline">Guiding - Bike Sport Events<br>MTB Fahrtechnik</h1>

  <div class="contact">
    <section>
      <h2 class="company">kurvenrad</h2>
      <p>Musterstraße 25/1</p>
      <p>12345 Musterstadt</p>
    </section>
    <section>
      <h2>Geschäftsführer</h2>
      <p>Max Mustermann</p>
      <p>Sitz: Musterstadt</p>
      <p>USt-IdNr: DE000111222</p>
    </section>
    <section>
      <h2>Kontakt</h2>
      <p>Tel.: 01234 5678901</p>
      <p>Fax: 01234 5678902</p>
      <p>www.kurvenrad.de</p>
      <p>info@kurvenrad.de</p>
    </section>
    <section>
      <h2>Bankverbindung</h2>
      <p>Talbank Nord</p>
      <p>BIC: TALB DEN1 KRV</p>
      <p>IBAN:</p>
      <p>DE00 1234 5678 9012 3456 78</p>
    </section>
  </div>

  <div class="footer-band"></div>
</div>
</body>
</html>
```